Tin-lantern-walk.com

The existing website http://www.tin-lantern-walk.com needs to get into shape. I'd like to have it transformed into wordpress with a brand-new design. The design should include a logo for multiple uses.

```html
<!DOCTYPE html>
<html lang="en">
<head>
<meta charset="utf-8">
<title>Tin-lantern-walk.com</title>
<link href="https://fonts.googleapis.com/css2?family=Carlito:wght@400;700&family=Lato:wght@400;700&display=swap" rel="stylesheet">
<style>
:root{
  --green:#358a0c;
  --green-bright:#3d9410;
  --white:#ffffff;
  --grey-bg:#e7e7e7;
  --text-dark:#333333;
  --hero-dark:#2b2d31;
}
*{margin:0;padding:0;box-sizing:border-box}
html,body{width:1109px;height:1200px;overflow:hidden}
body{position:relative;font-family:"Carlito",sans-serif;color:var(--white);background:var(--hero-dark)}
.abs{position:absolute}
.hero-photo{left:0;top:0;width:1109px;height:879px;
  background:radial-gradient(ellipse at 45% 40%,#4a4744 0%,#35363a 45%,#26282c 100%)}
.service-shade{left:0;top:461px;width:1109px;height:418px;
  background:linear-gradient(180deg,rgba(110,100,95,.55),rgba(80,75,75,.55))}
.header-rule{left:0;top:76px;width:1109px;height:1px;background:rgba(255,255,255,.15)}
.brand{left:53px;top:10px;width:140px;height:140px;border-radius:50%;background:var(--green);
  display:flex;align-items:center;justify-content:center;
  font-family:"Lato",sans-serif;font-weight:700;font-size:14px;color:var(--white)}
.nav a{position:absolute;top:31px;font-family:"Lato",sans-serif;font-size:11.5px;color:var(--white);text-decoration:none;transform:translateX(-50%);white-space:nowrap}
.nav .active{top:7px;width:63px;height:63px;border:1px solid var(--white);background:var(--green);border-radius:50%;
  display:flex;align-items:center;justify-content:center}
.arrow{width:38px;height:38px;border:2px solid var(--white);border-radius:50%}
.hero-title{left:0;width:1109px;top:232px;text-align:center;font-family:"Lato",sans-serif;font-size:61px;color:var(--green-bright);letter-spacing:-.5px}
.hero-sub{left:0;width:1109px;top:320px;text-align:center;font-family:"Lato",sans-serif;font-size:17px;line-height:26px}
.section-title{left:0;width:1109px;top:492px;text-align:center;font-family:"Lato",sans-serif;font-size:31px;color:var(--green-bright)}
.connector{height:2px;background:var(--white);top:623px}
.badge{width:130px;height:130px;top:557px;border-radius:50%;display:flex;align-items:center;justify-content:center}
.badge.light{background:var(--white)}
.badge.dark{background:var(--green)}
.card{width:260px;text-align:center}
.card h3{font-family:"Lato",sans-serif;font-weight:400;font-size:15px;color:var(--green-bright);text-transform:uppercase;margin-bottom:8px}
.card p{font-size:12px;line-height:15px}
.card .more{display:inline-block;margin-top:10px;font-size:12px;color:var(--white);text-decoration:none}
.card .more.hl{color:var(--green-bright)}
.about{left:0;top:879px;width:1109px;height:203px;background:var(--grey-bg);color:var(--text-dark);text-align:center}
.about h2{font-family:"Lato",sans-serif;font-weight:400;font-size:33px;color:var(--green);padding-top:25px}
.about p{font-size:11.5px;line-height:21px;margin-top:14px}
.btn{display:inline-block;margin-top:16px;width:124px;height:31px;line-height:31px;background:var(--green);color:var(--white);font-size:11.5px;text-decoration:none}
.footer{left:0;top:1082px;width:1109px;height:118px;background:var(--green)}
.footer-links{left:0;width:1117px;top:45px;text-align:center;font-size:11.5px}
.footer-links span{margin:0 5px}
.copyright{left:0;width:1117px;top:70px;text-align:center;font-size:9.5px}
.social{width:14px;height:14px;border-radius:50%;border:1.5px solid rgba(255,255,255,.8);top:55px}
</style>
</head>
<body>
<div class="abs hero-photo" role="img" aria-label="Darkened photo of a person outdoors reading a map in hilly country"></div>
<div class="abs service-shade"></div>
<div class="abs header-rule"></div>

<div class="abs brand">Tin-lantern-walk</div>

<nav class="nav">
  <a class="active" href="#" style="left:493px">CLAIM</a>
  <a href="#" style="left:575px">PROCESS</a>
  <a href="#" style="left:681px">RESPONSIBILITY</a>
  <a href="#" style="left:780px">COSTS</a>
  <a href="#" style="left:866px">FINISHING</a>
  <a href="#" style="left:959px">CONTACT</a>
  <a href="#" style="left:1041px">BLOG</a>
</nav>

<svg class="abs arrow" style="left:46px;top:242px" viewBox="0 0 38 38"><path d="M21 12l-7 7 7 7" fill="none" stroke="#fff" stroke-width="2.5"/></svg>
<svg class="abs arrow" style="left:1029px;top:241px" viewBox="0 0 38 38"><path d="M17 12l7 7-7 7" fill="none" stroke="#fff" stroke-width="2.5"/></svg>

<h1 class="abs hero-title">TIN-LANTERN-WALK.COM</h1>
<p class="abs hero-sub">Lorem ipsum dolor sit amet, consectetur adipiscing elit, sed do eiusmod tempor<br>incididunt ut labore et dolore magna aliqua</p>

<h2 class="abs section-title">Our Service</h2>
<div class="abs connector" style="left:290px;width:192px"></div>
<div class="abs connector" style="left:612px;width:170px"></div>

<div class="abs badge light" style="left:160px">
  <svg width="66" height="54" viewBox="0 0 66 54" fill="none" stroke="#358a0c" stroke-width="5" stroke-linejoin="round">
    <path d="M22 4l12 5v12l-12 5-12-5V9z"/><path d="M12 24l12 5v12l-12 5-12-5V29z"/><path d="M38 24l12 5v12l-12 5-12-5V29z"/><path d="M50 14l12 5v12"/>
  </svg>
</div>
<div class="abs badge dark" style="left:482px">
  <svg width="66" height="62" viewBox="0 0 66 62" fill="none" stroke="#fff" stroke-width="5">
    <path d="M30 4h20l10 10v34H30z"/><path d="M38 22h14M38 30h14M38 38h14"/><circle cx="26" cy="34" r="12"/><path d="M17 43L6 54"/>
  </svg>
</div>
<div class="abs badge dark" style="left:781px">
  <svg width="56" height="60" viewBox="0 0 56 60" fill="none" stroke="#fff" stroke-width="4">
    <rect x="4" y="10" width="48" height="46" rx="4"/><path d="M4 22h48M16 4v10M40 4v10"/>
    <text x="28" y="50" text-anchor="middle" fill="#fff" stroke="none" font-family="Lato,sans-serif" font-weight="700" font-size="24">15</text>
  </svg>
</div>

<div class="abs card" style="left:100px;top:700px">
  <h3>The demands on our work</h3>
  <p>Lorem ipsum dolor sit amet, consectetur edit<br>adipiscing elit, sed do eiusmod tempor<br>incididunt utdolore magna aliqua.</p>
  <a class="more hl" href="#">Read More &#9656;</a>
</div>
<div class="abs card" style="left:429px;top:700px">
  <h3>Our quality guarantee</h3>
  <p>Lorem ipsum dolor sit amet, consectetur edit<br>adipiscing elit, sed do eiusmod tempor<br>incididunt utdolore magna aliqua.</p>
  <a class="more" href="#">Read More &#9656;</a>
</div>
<div class="abs card" style="left:720px;top:700px">
  <h3>Success factor: efficiency</h3>
  <p>Lorem ipsum dolor sit amet, consectetur edit<br>adipiscing elit, sed do eiusmod tempor<br>incididunt utdolore a aliqua.</p>
  <a class="more" href="#">Read More &#9656;</a>
</div>

<section class="abs about">
  <h2>What are Escape and Rescue Plans?</h2>
  <p>It is burning. Now it is: get out of the building. To safety. Escape and rescue plans are an important guide and also an essential tool for training people for the right behavior in case of fire.<br>With the professional preparation of escape and rescue plans we contribute our part in ensuring that people with you in case of a fire in the shortest find ways out of the building.</p>
  <a class="btn" href="#">READ MORE</a>
</section>

<footer class="abs footer">
  <div class="abs footer-links">Home<span>/</span>Claim<span>/</span>Process<span>/</span>Responsibility<span>/</span>Finishing<span>/</span>Contact Us</div>
  <div class="abs copyright">&copy; All Rights Reserved. Copyrights @Tin-lantern-walk 2016</div>
  <div class="abs social" style="left:901px" aria-label="Feed"></div>
  <div class="abs social" style="left:936px" aria-label="Social link"></div>
  <div class="abs social" style="left:971px" aria-label="Social link"></div>
  <div class="abs social" style="left:1006px" aria-label="Social link"></div>
  <div class="abs social" style="left:1041px" aria-label="Social link"></div>
</footer>
</body>
</html>
```